Drink Product Brochure

We have 3 tea drinks in plastic bottles that we'd like to put in a brochure (8"x11" sheet) and focus on all natural, no preservatives, and supporting a nonprofit orphanage. The logo boasts a one color design - green. The brochure should make 3-4 key highlights, and allow at least one section product overview. Clean, modern design with not to many distractions but an inviting natural look and highlight the key features.

Target Market(s)

Middle age

Font styles to use
Serif
Sans Serif

Colors
add136
85cae6
b768aa

```html
<!DOCTYPE html>
<html lang="en">
<head>
<meta charset="utf-8">
<title>Meadowbrook Tea – Trifold Brochure</title>
<link href="https://fonts.googleapis.com/css2?family=Montserrat:wght@600;700;800&family=Lora:wght@400;600&family=Dancing+Script:wght@700&display=swap" rel="stylesheet">
<style>
  :root{
    --green-deep:#2f8a35;
    --green:#3f9f3c;
    --green-lime:#add136;
    --sky:#85cae6;
    --berry:#b768aa;
    --paper:#ffffff;
    --ink:#3d4a3f;
    --ink-soft:#eaf5e4;
    --bg:#e9eaeb;
  }
  *{box-sizing:border-box;margin:0;padding:0}
  html,body{width:851px;height:1200px;overflow:hidden;background:var(--bg)}
  body{font-family:"Lora",Georgia,serif;color:var(--ink);position:relative}
  .spread{position:absolute;left:45px;width:760px;height:560px;display:grid;grid-template-columns:repeat(3,1fr);background:var(--paper);box-shadow:0 6px 18px rgba(0,0,0,.18);overflow:hidden}
  .spread--outside{top:30px}
  .spread--inside{top:612px;background:var(--green)}
  .panel{position:relative;overflow:hidden;border-right:1px solid rgba(0,0,0,.06)}
  .panel:last-child{border-right:0}
  .photo{position:absolute;left:0;right:0}
  .wave{position:absolute;left:0;width:100%}
  .heading{font-family:"Montserrat",Arial,sans-serif;font-weight:800;color:var(--green-deep);text-transform:uppercase;line-height:1.15}
  .body-copy{font-size:9.5px;line-height:1.55}
  .pill{position:absolute;left:50%;transform:translateX(-50%);background:var(--green);color:#fff;font-family:"Montserrat",Arial,sans-serif;font-weight:600;font-size:9px;padding:5px 18px;border-radius:12px;white-space:nowrap}
  .foot-band{position:absolute;left:0;right:0;bottom:0;height:22px;background:var(--green)}

  /* outside: orphanage flap */
  .flap .photo{top:0;height:262px;background:linear-gradient(160deg,#8fbf6a,#cfd9c2 45%,#6f8f5a)}
  .flap .heading{position:absolute;top:302px;left:20px;right:16px;font-size:15px}
  .flap .body-copy{position:absolute;top:348px;left:20px;right:18px}
  .flap .pill{bottom:40px}

  /* outside: back panel */
  .back{background:var(--green)}
  .back .intro{position:absolute;top:38px;left:24px;right:24px;color:#fff;text-align:center}
  .back .contact{position:absolute;top:250px;left:0;right:0;height:200px;background:var(--paper);text-align:center;padding-top:36px}
  .contact .label{font-family:"Montserrat",Arial,sans-serif;font-weight:700;font-size:11px;color:var(--green-deep);text-transform:uppercase;margin-bottom:8px}
  .contact p{font-size:9.5px;line-height:1.6}

  /* outside: cover */
  .cover .brand{position:absolute;top:0;right:18px;background:var(--paper);padding:10px 12px 8px;z-index:2;display:flex;align-items:center;gap:6px;font-family:"Montserrat",Arial,sans-serif;font-weight:700;font-size:11px;color:var(--green-deep)}
  .brand .mark{width:10px;height:10px;background:var(--green)}
  .cover .photo{top:0;height:300px;background:linear-gradient(150deg,#c9d8b0,#8a5a2e 45%,#b7c98a 70%,#5e3a1e)}
  .cover .tagline{position:absolute;top:350px;left:0;right:0;text-align:center}
  .tagline .script{font-family:"Dancing Script",cursive;font-size:40px;color:var(--green)}
  .tagline .caps{font-family:"Montserrat",Arial,sans-serif;font-weight:700;font-size:15px;letter-spacing:1px;color:var(--green-deep);margin-top:2px}
  .cover .pill{bottom:52px}

  /* inside */
  .inside-photos{position:absolute;top:0;left:0;right:0;height:232px;display:grid;grid-template-columns:repeat(3,1fr)}
  .inside-photos .shot--lemon{background:linear-gradient(160deg,#f3f1d8,#c7d77a 55%,#e8ecd8)}
  .inside-photos .shot--black{background:linear-gradient(160deg,#e6dcc4,#a8652b 55%,#d8e0c8)}
  .inside-photos .shot--orange{background:linear-gradient(160deg,#f4e3c8,#e07a32 50%,#b3c67a)}
  .spread--inside .wave{top:200px;z-index:1}
  .spread--inside .panel{border-right-color:rgba(0,0,0,.12)}
  .product{position:relative;z-index:2;color:#fff}
  .product .bottle{position:absolute;top:288px;left:16px;width:66px;height:132px;border-radius:10px 10px 6px 6px}
  .bottle--black{background:linear-gradient(#c94a3a,#8a2a22)}
  .bottle--berry{background:linear-gradient(var(--berry),#6e3560)}
  .bottle--peach{background:linear-gradient(#d9a24a,#8a5a22)}
  .product .feature{position:absolute;top:292px;left:94px;right:14px}
  .product .heading{color:#fff;font-size:11px;margin-bottom:6px}
  .product .body-copy{font-size:9px;color:var(--ink-soft)}
  .product .range{position:absolute;top:442px;left:16px;right:16px}
  .range .name{font-family:"Montserrat",Arial,sans-serif;font-weight:700;font-size:11px;color:var(--green-lime);text-transform:uppercase;margin-bottom:5px}
  .range ul{list-style:none}
  .range li{font-size:9.5px;line-height:1.65;padding-left:14px;position:relative}
  .range li::before{content:"";position:absolute;left:0;top:5px;width:7px;height:4px;border-left:2px solid var(--green-lime);border-bottom:2px solid var(--green-lime);transform:rotate(-45deg)}
</style>
</head>
<body>

<section class="spread spread--outside">
  <article class="panel flap">
    <div class="photo" role="img" aria-label="Photo of volunteers and children gathered outdoors at a table"></div>
    <svg class="wave" style="top:228px" viewBox="0 0 254 70" preserveAspectRatio="none" height="70">
      <path d="M0 30 C70 0 150 55 254 18 L254 70 L0 70Z" fill="#add136"/>
      <path d="M0 42 C80 14 160 66 254 30 L254 70 L0 70Z" fill="#3f9f3c"/>
      <path d="M0 56 C80 34 170 74 254 48 L254 70 L0 70Z" fill="#ffffff"/>
    </svg>
    <h2 class="heading">Supporting a<br>nonprofit orphanage</h2>
    <p class="body-copy">Every bottle you buy helps fund meals, schooling and care for children at a small orphanage we have partnered with since our very first batch. Sip well, give back.</p>
    <span class="pill">www.meadowbrooktea.com</span>
    <div class="foot-band"></div>
  </article>

  <article class="panel back">
    <p class="intro body-copy">Brewed in small batches from whole leaves, fresh fruit and pure cane sugar. Nothing artificial and no preservatives, just honest tea made the slow way, bottled cold so every sip tastes like it came straight from the kettle.</p>
    <svg class="wave" style="top:222px" viewBox="0 0 254 40" preserveAspectRatio="none" height="40">
      <path d="M0 28 C90 4 170 40 254 14 L254 40 L0 40Z" fill="#ffffff"/>
    </svg>
    <div class="contact">
      <p class="label">Find us at</p>
      <p>Meadowbrook Tea Co.<br>1200 Orchard Lane<br>Springfield, OR 97400<br>(555) 014-2288<br>hello@meadowbrooktea.com</p>
    </div>
    <div class="foot-band"></div>
  </article>

  <article class="panel cover">
    <div class="brand"><span class="mark"></span>Meadowbrook Tea</div>
    <div class="photo" role="img" aria-label="Photo of three bottled teas beside a glass of iced tea with lemon"></div>
    <svg class="wave" style="top:268px" viewBox="0 0 254 60" preserveAspectRatio="none" height="60">
      <path d="M0 20 C90 50 170 0 254 24 L254 60 L0 60Z" fill="#3f9f3c"/>
      <path d="M0 34 C90 60 170 14 254 38 L254 60 L0 60Z" fill="#ffffff"/>
    </svg>
    <div class="tagline">
      <p class="script">Refreshing</p>
      <p class="caps">YOUR SOUL AND MIND</p>
    </div>
    <span class="pill">www.meadowbrooktea.com</span>
    <div class="foot-band"></div>
  </article>
</section>

<section class="spread spread--inside">
  <div class="inside-photos">
    <div class="shot--lemon" role="img" aria-label="Photo of lemonade glasses with mint leaves"></div>
    <div class="shot--black" role="img" aria-label="Photo of a jar of iced black tea"></div>
    <div class="shot--orange" role="img" aria-label="Photo of iced tea with sliced oranges"></div>
  </div>
  <svg class="wave" viewBox="0 0 760 70" preserveAspectRatio="none" width="760" height="70">
    <path d="M0 30 C200 0 420 60 760 12 L760 70 L0 70Z" fill="#add136"/>
    <path d="M0 44 C220 14 440 70 760 28 L760 70 L0 70Z" fill="#3f9f3c"/>
  </svg>

  <article class="panel product">
    <div class="bottle bottle--black" role="img" aria-label="Photo of the classic black tea bottle"></div>
    <div class="feature">
      <h3 class="heading">All natural</h3>
      <p class="body-copy">Whole-leaf tea and real fruit, brewed simply with nothing artificial added.</p>
    </div>
    <div class="range">
      <p class="name">Classic Black Tea</p>
      <ul><li>Bold whole-leaf brew</li><li>Lightly sweetened</li><li>No preservatives</li></ul>
    </div>
  </article>

  <article class="panel product">
    <div class="bottle bottle--berry" role="img" aria-label="Photo of the berry hibiscus tea bottle"></div>
    <div class="feature">
      <h3 class="heading">No preservatives</h3>
      <p class="body-copy">Cold bottled fresh so the flavour stays bright without any additives.</p>
    </div>
    <div class="range">
      <p class="name">Berry Hibiscus Tea</p>
      <ul><li>Tart and fruity</li><li>Caffeine free</li><li>Real berry juice</li></ul>
    </div>
  </article>

  <article class="panel product">
    <div class="bottle bottle--peach" role="img" aria-label="Photo of the peach green tea bottle"></div>
    <div class="feature">
      <h3 class="heading">Giving back</h3>
      <p class="body-copy">A share of every bottle supports children at our partner orphanage.</p>
    </div>
    <div class="range">
      <p class="name">Peach Green Tea</p>
      <ul><li>Smooth and mellow</li><li>Ripe peach notes</li><li>Pure cane sugar</li></ul>
    </div>
  </article>
</section>

</body>
</html>
```